Wordpress template re-design of current website

We need a WordPress template design and new look for our existing website. Our existing site it located at www.velmoro.com.au We are a tech company and want a fresh, clean modern website that matches our brand, services and logo colors. Our main Services are hospitality solutions, Velmoro TV solution and managed networks, more information on these can come from our existing website.

Target Market(s)

We are a tech company so must have a modern feel for new technology

Industry/Entity Type

It Company

Number of Pages Required

5+ page

Font styles to use
Sans Serif

Requirements
Must have
• Be based on a wordpress templete design and match the services that we have in our existing website, in the testimonials want a place for video testimonials as well as text. Nice clean icons used for graphics to represent services.
Nice to have
• nice visual representation of our services in the way of clean icons etc
Should not have
• Clutter

```html
<!DOCTYPE html>
<html lang="en">
<head>
<meta charset="utf-8">
<title>Velmoro Wireless Internet</title>
<link rel="stylesheet" href="https://fonts.googleapis.com/css2?family=Lato:wght@400;700&display=swap">
<style>
:root{
  --blue:#0b4a8b;
  --blue-dark:#083a6e;
  --grey-band:#ebebeb;
  --grey-icon:#5f6368;
  --grey-text:#6b6b6b;
  --text:#333;
  --page:#e4e6ea;
  --white:#fff;
  --footer-bar:#6f747a;
}
*{margin:0;padding:0;box-sizing:border-box}
html,body{width:1200px;height:2333px;overflow:hidden}
body{background:var(--page);font-family:'Lato',sans-serif;color:var(--text);position:relative}
.site{position:absolute;left:107px;top:0;width:985px;height:2333px;background:var(--white);box-shadow:0 0 14px rgba(0,0,0,.15)}
.abs{position:absolute}
/* header */
.logo{left:65px;top:16px;display:flex;align-items:center;gap:8px}
.logo-name{font-size:32px;color:var(--blue);font-weight:400;line-height:1}
.logo-dot{width:18px;height:18px;border-radius:50%;background:var(--blue)}
.nav{left:403px;top:29px;display:flex;gap:0;font-size:13px;color:var(--grey-text)}
.nav a{color:inherit;text-decoration:none;margin-right:31px}
.nav a.active{color:var(--blue);font-weight:700}
.btn{background:var(--blue);color:var(--white);font-size:13px;font-weight:700;border-radius:3px;display:flex;align-items:center;justify-content:center;text-decoration:none}
.portal{left:828px;top:27px;width:93px;height:28px}
/* hero */
.hero{left:0;top:80px;width:985px;height:350px;background:linear-gradient(100deg,#d9c6a6 0%,#b9875a 35%,#a2301f 55%,#8a5a38 70%,#c9d6e0 85%,#6d4b35 100%)}
.hero-title{left:0;top:148px;width:985px;text-align:center;font-size:33px;color:var(--white);text-shadow:0 1px 3px rgba(0,0,0,.45)}
.hero-link{left:0;top:196px;width:985px;text-align:center;font-size:15px;font-weight:700;color:var(--white);text-decoration:underline}
.contact-tab{right:0;top:80px;width:275px;height:45px;background:var(--footer-bar);clip-path:polygon(25px 0,100% 0,100% 100%,0 100%,0 50%);display:flex;align-items:center;padding-left:52px;color:var(--white);font-size:14px;gap:10px}
.tab-sep{width:1px;height:22px;background:rgba(255,255,255,.6);margin:0 10px}
.soc{width:11px;height:11px;border-radius:50%;background:var(--white);margin-right:10px}
.slide-arrow{top:238px;width:22px;height:37px;background:rgba(220,220,220,.85);display:flex;align-items:center;justify-content:center}
/* services */
.card{top:430px;width:205px;height:192px;background:#f2f2f2;box-shadow:0 8px 8px -4px rgba(0,0,0,.18);text-align:center}
.card-icon{position:absolute;left:52px;top:-55px;width:100px;height:100px;border-radius:50%;border:4px solid var(--white);box-shadow:0 2px 5px rgba(0,0,0,.25);background:var(--grey-icon);display:flex;align-items:center;justify-content:center}
.card.featured .card-icon{background:var(--blue)}
.card-title{position:absolute;top:61px;width:100%;font-size:14.5px;color:#7a7a7a}
.card.featured .card-title{color:var(--blue)}
.card-text{position:absolute;top:91px;left:10px;right:10px;font-size:10.5px;line-height:16px;color:#444}
.card-more{position:absolute;top:153px;left:0;width:100%;display:flex;justify-content:center;align-items:center;gap:9px;font-size:11px;color:#888}
.card.featured .card-more{color:var(--blue);font-weight:700}
.more-box{width:20px;height:20px;background:var(--grey-icon);border-radius:2px;display:flex;align-items:center;justify-content:center}
.card.featured .more-box{background:var(--blue)}
/* sections */
.band{left:0;width:985px}
.band.grey{background:var(--grey-band)}
.h2{font-size:24px;color:var(--blue);font-weight:400}
.about-text{left:65px;top:92px;width:860px;font-size:11.5px;line-height:17px;color:#444}
.about-text p+p{margin-top:16px}
.gal{background:#8a8f95}
.gal-feature{left:598px;top:100px;width:323px;height:303px;background:linear-gradient(180deg,#3b6aa6,#1f4f8f);display:flex;align-items:center;justify-content:center;text-align:center;color:var(--white);font-size:19px;font-weight:700;line-height:24px}
.video{left:65px;top:94px;width:268px;height:150px;background:linear-gradient(135deg,#2c2c2c,#111)}
.play{left:111px;top:52px;width:48px;height:48px;border-radius:50%;border:3px solid var(--white)}
.video-cap{left:0;bottom:8px;width:268px;text-align:center;color:var(--white);font-size:13px}
.quote{left:343px;top:94px;width:578px;height:150px;background:var(--white);padding:14px 24px 0 18px;font-size:11.5px;line-height:17px;color:#444}
.quote-mark{font-size:54px;color:#ddd;line-height:1;position:absolute;font-family:'Lato',sans-serif}
.quote-by{color:var(--blue);font-size:13px;margin-top:8px}
.clients{left:65px;top:93px;width:856px;height:100px;border:1px solid #bbb;display:flex;align-items:center;justify-content:space-around}
.client{display:flex;align-items:center;gap:6px;font-size:18px;font-weight:700;color:#444}
.client i{display:block;width:12px;height:12px;background:var(--blue)}
/* footer */
.footer{left:0;top:2113px;width:985px;height:189px;background:var(--blue);color:var(--white)}
.f-head{font-size:13px;font-weight:700}
.f-list{font-size:11.5px;line-height:22.5px;list-style:none}
.f-sep{width:1px;background:rgba(255,255,255,.3);top:42px;height:120px}
.f-rule{height:1px;background:rgba(255,255,255,.25);width:150px}
.copy{left:0;top:2302px;width:985px;height:31px;background:var(--footer-bar);color:var(--white);font-size:11px;font-weight:700;display:flex;align-items:center;justify-content:center}
</style>
</head>
<body>
<div class="site">
  <header>
    <div class="abs logo"><span class="logo-name">Velmoro</span><span class="logo-dot"></span></div>
    <nav class="abs nav"><a class="active" href="#">Home</a><a href="#">About Us</a><a href="#">Services</a><a href="#">Work Gallery</a><a href="#">Contact Us</a></nav>
    <a class="abs btn portal" href="#">PORTAL</a>
  </header>

  <section>
    <div class="abs hero" role="img" aria-label="Photograph of a hotel bedroom with a red bedspread and a balcony view to the sea"></div>
    <div class="abs contact-tab">
      <svg width="16" height="16" viewBox="0 0 24 24"><path fill="#fff" d="M6.6 10.8a15 15 0 0 0 6.6 6.6l2.2-2.2c.3-.3.7-.4 1-.2 1.1.4 2.3.6 3.6.6.6 0 1 .4 1 1V20c0 .6-.4 1-1 1A17 17 0 0 1 3 4c0-.6.4-1 1-1h3.5c.6 0 1 .4 1 1 0 1.3.2 2.5.6 3.6.1.3 0 .7-.2 1z"/></svg>
      <span>1300 555 014</span><span class="tab-sep"></span><span class="soc"></span><span class="soc"></span>
    </div>
    <div class="abs slide-arrow" style="left:0"><svg width="10" height="14" viewBox="0 0 10 14"><path d="M8 1 2 7l6 6" fill="none" stroke="#333" stroke-width="2.5"/></svg></div>
    <div class="abs slide-arrow" style="right:0"><svg width="10" height="14" viewBox="0 0 10 14"><path d="m2 1 6 6-6 6" fill="none" stroke="#333" stroke-width="2.5"/></svg></div>
    <h1 class="abs hero-title" style="font-weight:400">Hospitality Solutions</h1>
    <a class="abs hero-link" href="#">Read More</a>
  </section>

  <section>
    <div class="abs card featured" style="left:65px">
      <div class="card-icon"><svg width="42" height="42" viewBox="0 0 42 42" fill="#fff"><rect x="8" y="4" width="26" height="34"/><g fill="#0b4a8b"><rect x="12" y="9" width="4" height="4"/><rect x="19" y="9" width="4" height="4"/><rect x="26" y="9" width="4" height="4"/><rect x="12" y="16" width="4" height="4"/><rect x="19" y="16" width="4" height="4"/><rect x="26" y="16" width="4" height="4"/><rect x="12" y="23" width="4" height="4"/><rect x="19" y="23" width="4" height="4"/><rect x="26" y="23" width="4" height="4"/><rect x="18" y="30" width="6" height="8"/></g></svg></div>
      <div class="card-title">Hospitality Solutions</div>
      <div class="card-text">Lorem ipsum dolor sit amet, consect etuer adipiscing elit, sed diam nonu mmy nibh euismod tincidunt</div>
      <div class="card-more"><span class="more-box"><svg width="8" height="10" viewBox="0 0 8 10"><path d="m1 1 5 4-5 4" fill="none" stroke="#fff" stroke-width="2"/></svg></span>Read More</div>
    </div>
    <div class="abs card" style="left:281px">
      <div class="card-icon"><svg width="44" height="40" viewBox="0 0 44 40"><rect x="3" y="4" width="38" height="26" rx="3" fill="none" stroke="#fff" stroke-width="3.5"/><rect x="16" y="32" width="12" height="3" fill="#fff"/><rect x="12" y="35" width="20" height="3" fill="#fff"/></svg></div>
      <div class="card-title">Velmoro TV Solution</div>
      <div class="card-text">Lorem ipsum dolor sit amet, consect etuer adipiscing elit, sed diam nonu mmy nibh euismod tincidunt</div>
      <div class="card-more"><span class="more-box"><svg width="8" height="10" viewBox="0 0 8 10"><path d="m1 1 5 4-5 4" fill="none" stroke="#fff" stroke-width="2"/></svg></span>Read More</div>
    </div>
    <div class="abs card" style="left:498px">
      <div class="card-icon"><svg width="44" height="36" viewBox="0 0 44 36" fill="none" stroke="#fff" stroke-width="4" stroke-linecap="round"><path d="M4 12a26 26 0 0 1 36 0"/><path d="M10 19a17 17 0 0 1 24 0"/><path d="M16 26a8 8 0 0 1 12 0"/><circle cx="22" cy="32" r="2" fill="#fff"/></svg></div>
      <div class="card-title">Managed Networks</div>
      <div class="card-text">Lorem ipsum dolor sit amet, consect etuer adipiscing elit, sed diam nonu mmy nibh euismod tincidunt</div>
      <div class="card-more"><span class="more-box"><svg width="8" height="10" viewBox="0 0 8 10"><path d="m1 1 5 4-5 4" fill="none" stroke="#fff" stroke-width="2"/></svg></span>Read More</div>
    </div>
    <div class="abs card" style="left:716px">
      <div class="card-icon"><svg width="26" height="42" viewBox="0 0 26 42"><rect x="2" y="2" width="22" height="38" rx="3" fill="none" stroke="#fff" stroke-width="3"/><rect x="6" y="7" width="14" height="25" fill="#fff"/><circle cx="13" cy="36" r="1.8" fill="#fff"/></svg></div>
      <div class="card-title">Mobile Solution</div>
      <div class="card-text">Lorem ipsum dolor sit amet, consect etuer adipiscing elit, sed diam nonu mmy nibh euismod tincidunt</div>
      <div class="card-more"><span class="more-box"><svg width="8" height="10" viewBox="0 0 8 10"><path d="m1 1 5 4-5 4" fill="none" stroke="#fff" stroke-width="2"/></svg></span>Read More</div>
    </div>
    <a class="abs btn" href="#" style="left:445px;top:655px;width:96px;height:27px">View All</a>
  </section>

  <section class="abs band grey" style="top:735px;height:280px">
    <h2 class="abs h2" style="left:68px;top:48px">About Us</h2>
    <div class="abs about-text">
      <p>Velmoro Wireless is at the forefront of revolutionising high-speed internet access (HSIA) services. We offer complete wireless solutions: Right from developing individual components such as hotspots and access controllers, to installation of the internet infrastructure. Once we setup the HSIA for our clients, we back it up with round-the-clock tech support.</p>
      <p>Velmoro's expertise in wireless technology has attracted a growing client base from all over Australia.</p>
    </div>
    <a class="abs btn" href="#" style="left:823px;top:202px;width:97px;height:26px">Read More</a>
  </section>

  <section class="abs band" style="top:1015px;height:508px">
    <h2 class="abs h2" style="left:65px;top:52px">Work Gallery</h2>
    <div class="abs gal" style="left:65px;top:100px;width:220px;height:147px;background:linear-gradient(180deg,#dfe6ea,#c8cdd0 60%,#5d6a50)" role="img" aria-label="Photograph of a white tour coach parked on a street"></div>
    <div class="abs gal" style="left:295px;top:100px;width:293px;height:147px;background:linear-gradient(135deg,#8a6a56,#6e5a4e 50%,#9a7b66)" role="img" aria-label="Aerial photograph of a remote township"></div>
    <div class="abs gal" style="left:66px;top:255px;width:255px;height:148px;background:linear-gradient(180deg,#1d3a6e,#2d5a94 60%,#2a2f2a)" role="img" aria-label="Photograph of an apartment building at dusk among trees"></div>
    <div class="abs gal" style="left:331px;top:255px;width:257px;height:148px;background:linear-gradient(135deg,#3a2f28,#6b5a4a 50%,#b8b0a6)" role="img" aria-label="Photograph of a laptop and a smartphone showing a hotel portal"></div>
    <div class="abs gal-feature" role="img" aria-label="Photograph of a modern apartment tower with a blue overlay"><span>Harbourview Kelvin Grove Opened<br>September 2014</span></div>
    <a class="abs btn" href="#" style="left:825px;top:428px;width:96px;height:29px">View All</a>
  </section>

  <section class="abs band grey" style="top:1523px;height:349px">
    <h2 class="abs h2" style="left:65px;top:52px">Client Testimonials</h2>
    <div class="abs video" role="img" aria-label="Video still of a property manager speaking">
      <div class="abs play"></div>
      <svg class="abs" style="left:130px;top:67px" width="14" height="18" viewBox="0 0 14 18"><path d="M1 1l12 8-12 8z" fill="#fff"/></svg>
      <div class="abs video-cap">Tom Reilly - Property Manager</div>
    </div>
    <div class="abs quote">
      <span class="quote-mark" style="left:8px;top:4px">&ldquo;</span>
      <span class="quote-mark" style="right:20px;top:96px">&rdquo;</span>
      <p style="text-indent:28px">Installing Velmoro Internet Solution has been a great investment for this business. The staff were very professional and easy to work with and gave us several options to consider that would work best for the business. The installation was easy and happened without any problems at all. The system is easy to use for both guests and staff, which can be tailored to suit the needs of the guest and business, which was a deciding factor. I would highly recommend Velmoro as you're in room internet solution</p>
      <p class="quote-by">Paul Hendry &ndash; Lakeside Suites Bendigo</p>
    </div>
    <a class="abs btn" href="#" style="left:825px;top:270px;width:96px;height:27px">View All</a>
  </section>

  <section class="abs band" style="top:1872px;height:241px">
    <h2 class="abs h2" style="left:65px;top:52px">Our Client</h2>
    <svg class="abs" style="left:893px;top:56px" width="30" height="16" viewBox="0 0 30 16" fill="none" stroke="#0b4a8b" stroke-width="2.5"><path d="M8 2 2 8l6 6"/><path d="m22 2 6 6-6 6"/></svg>
    <div class="abs clients">
      <span class="client"><i></i>Northway</span>
      <span class="client"><i></i>Ashgrove</span>
      <span class="client">Kestrel Mining</span>
      <span class="client"><i></i>Wanderly</span>
      <span class="client">Corvan</span>
      <span class="client">Trekline</span>
    </div>
  </section>

  <footer>
    <div class="abs footer">
      <div class="abs" style="left:65px;top:23px">
        <div class="f-head">QUICK LINKS</div>
        <ul class="f-list" style="margin-top:9px;padding-left:4px">
          <li>&bull; Home</li><li>&bull; About Us</li><li>&bull; Services</li><li>&bull; Work Gallery</li><li>&bull; Contact Us</li>
        </ul>
      </div>
      <div class="abs f-sep" style="left:268px"></div>
      <div class="abs" style="left:281px;top:23px;font-size:11.5px">
        <div class="f-head">CONTACT DETAILS</div>
        <p style="margin-top:14px;line-height:17px;font-weight:700">42 Harbour Crescent<br>Coral Bay, QLD 4210</p>
        <div class="f-rule" style="margin-top:9px"></div>
        <p style="margin-top:12px;font-weight:700">Ph :&nbsp; 1300 555 014</p>
        <div class="f-rule" style="margin-top:12px"></div>
        <p style="margin-top:15px;font-weight:700">E-mail :&nbsp; sales@velmoro.com.au</p>
      </div>
      <div class="abs f-sep" style="left:500px"></div>
      <ul class="abs f-list" style="left:560px;top:47px;line-height:31px;font-weight:700">
        <li>&gt; Case Studies</li><li>&gt; Testimonials</li><li>&gt; News</li><li>&gt; Resellers</li>
      </ul>
      <div class="abs f-sep" style="left:720px"></div>
      <div class="abs" style="left:780px;top:50px;display:flex;align-items:center;gap:8px">
        <span style="font-size:30px">Velmoro</span><span style="width:16px;height:16px;border-radius:50%;background:#fff"></span>
      </div>
      <div class="abs" style="left:778px;top:139px;display:flex;align-items:center;gap:12px;font-size:13px;font-weight:700">
        <span>FOLLOW US :</span><span class="soc" style="margin:0"></span><span class="soc" style="margin:0"></span>
      </div>
    </div>
    <div class="abs copy">&copy; 2015 Velmoro. All Rights Reserved.</div>
  </footer>
</div>
</body>
</html>
```